Velvet Crest Club Members Site

To design a website template that is mobile and desktop friendly for the high net worth members, inner circle club for the rich.
Design of the website must be of luxury feel, a club for the rich.
This website offers redemption of luxury items such as travel packages, and many other items.

Below are the page templates required:

MEMBER SITE

- Login Page
- Dashboard Page (Consists of the member’s redemption points summary, expiry dates)
- Categories Page (The main categories of luxury to redeem)
- Product Page (The actual product details to redeem, showing price, description, title, remarks)
- Redemption Cart (Like a shopping cart which temporary stores the selected items for redemption)
- Checkout Page (Like shopping cart checkout to confirm redemption, fill in address, contact number, name)
- Redemption History (Show a list of items redeemed, with the redemption points used, date)
- Redemption Product Page (Show the redeem product’s details like price, description, title, remarks, date redeemed, points used)
- Inbox (Messaging towards customer service/support)
- Write Message Page
- Read Message Page
- Change Password Page
- My Profile Page

ADMIN SITE

- Login Page
- Dashboard Page (Consists of the whole system redemption points summary in the whole club)
- Redemption Page (To Approve or Cancel Redemptions, or message member to ask more about the redemption)
- Administrator List (List the admins in the system)
- Change Password Page
- Inbox (Messaging towards customer)
- Write Message Page
- Read Message Page
- My Profile Page
- Product Management -> Product List Page, Add/Remove/Edit Product Page
- Category Management -> Category List Page, Add/Remove/Edit Category Page

Note:
All colours should be easily changeable under one css file.
You are feel to use colour tones that reflect high society, rich inner circle club.
The website must be mobile friendly.

Reason: Logo of website uploaded in project brief, pls use the colours tone from the logo. Thanks.

Target Market(s)

High Networth Individuals

Industry/Entity Type

Club

Coding

Coded - Design and coding required

Number of Pages Required

5+ page

Font styles to use
Serif
Sans Serif
Decorative
Script

Requirements
Must have
• It must be desktop and mobile friendly
• All colours should be easily changeable under one css file.

```html
<!DOCTYPE html>
<html lang="en">
<head>
<meta charset="utf-8">
<title>Luxury Getaway – Velvet Crest Club</title>
<link href="https://fonts.googleapis.com/css2?family=Open+Sans:wght@400;500;600;700&display=swap" rel="stylesheet">
<style>
  :root {
    --ink: #333333;
    --ink-soft: #8a8a8a;
    --accent: #2f7dc6;
    --accent-dark: #2a6fb2;
    --teal: #1fb8c9;
    --rule: #c8c8c8;
    --page: #ffffff;
    --hero-top: #4f8fd6;
    --hero-mid: #2a66ad;
    --hero-bottom: #8c8672;
  }
  * { box-sizing: border-box; margin: 0; padding: 0; }
  html, body {
    width: 1200px; height: 1000px; overflow: hidden;
    background: var(--page);
    font-family: "Open Sans", Arial, sans-serif;
    color: var(--ink);
  }
  a { color: var(--accent); text-decoration: none; }
  .site { position: relative; width: 1200px; height: 1000px; }

  /* header */
  .site-header { position: absolute; left: 75px; right: 87px; top: 50px; height: 70px; }
  .brand { position: absolute; left: 0; top: 8px; display: flex; align-items: center; gap: 12px; }
  .brand-mark { width: 40px; height: 40px; background: var(--teal); }
  .brand-name { font-size: 30px; font-weight: 700; color: var(--ink); letter-spacing: 1px; }
  .account { position: absolute; right: 0; top: 1px; display: flex; align-items: center; gap: 18px; font-size: 19.5px; color: #666; }
  .inbox-icon { position: relative; width: 26px; height: 20px; }
  .inbox-count {
    position: absolute; left: -9px; top: -10px; width: 18px; height: 18px; border-radius: 50%;
    background: var(--teal); color: #fff; font-size: 11px; font-weight: 600;
    display: flex; align-items: center; justify-content: center;
  }
  .main-nav { position: absolute; right: 0; top: 43px; display: flex; align-items: center; gap: 24px; font-size: 19px; font-weight: 600; }
  .main-nav a { color: var(--ink); }
  .main-nav a.is-current { color: var(--accent); }

  /* page heading */
  .page-title { position: absolute; left: 72px; top: 157px; font-size: 25px; font-weight: 400; }
  .title-rule { position: absolute; left: 73px; width: 1042px; top: 198px; border-top: 1px solid var(--rule); }
  .breadcrumb { position: absolute; left: 74px; top: 206px; font-size: 16px; font-weight: 600; color: var(--ink-soft); display: flex; align-items: center; gap: 8px; }
  .breadcrumb .sep { font-size: 9px; color: #777; }

  /* hero */
  .hero {
    position: absolute; left: 72px; top: 250px; width: 1046px; height: 333px;
    background: linear-gradient(180deg, var(--hero-top) 0%, var(--hero-mid) 60%, var(--hero-bottom) 100%);
  }

  /* product */
  .product-title { position: absolute; left: 70px; top: 604px; font-size: 33px; font-weight: 500; }
  .location { position: absolute; left: 72px; top: 653px; font-size: 21px; font-weight: 600; color: var(--ink-soft); display: flex; align-items: center; gap: 8px; }
  .price { position: absolute; right: 80px; top: 602px; display: flex; align-items: baseline; gap: 10px; }
  .price-label { font-size: 18px; color: var(--ink-soft); }
  .price-value { font-size: 32px; color: var(--accent); }
  .book-btn {
    position: absolute; right: 82px; top: 648px; width: 137px; height: 30px;
    background: var(--accent); border: 1px solid var(--accent-dark); color: #fff;
    font-size: 17px; font-weight: 600; display: flex; align-items: center; justify-content: center;
  }
  .description { position: absolute; left: 70px; width: 1055px; font-size: 16px; font-weight: 600; line-height: 22px; }
  .description.intro { top: 699px; }
  .description.outro { top: 870px; left: 67px; width: 1000px; }
  .features { position: absolute; left: 88px; top: 779px; list-style: none; font-size: 18.5px; font-weight: 600; color: var(--ink-soft); }
  .features li { display: flex; align-items: center; gap: 10px; height: 25.5px; }
  .features li::before {
    content: ""; width: 0; height: 0;
    border-left: 12px solid var(--accent); border-top: 7px solid transparent; border-bottom: 7px solid transparent;
  }

  /* footer */
  .footer-rule { position: absolute; left: 74px; width: 1040px; top: 942px; border-top: 1px solid var(--rule); }
  .copyright { position: absolute; left: 76px; top: 955px; font-size: 15.5px; font-weight: 600; color: var(--ink-soft); }
  .footer-nav { position: absolute; right: 86px; top: 953px; display: flex; gap: 20px; font-size: 16px; font-weight: 600; }
  .footer-nav a { color: var(--ink); }
</style>
</head>
<body>
<div class="site">
  <header class="site-header">
    <div class="brand">
      <span class="brand-mark"></span>
      <span class="brand-name">Velvet Crest Club</span>
    </div>
    <div class="account">
      <span class="inbox-icon">
        <svg width="26" height="20" viewBox="0 0 26 20"><rect x="1" y="4" width="24" height="15" fill="#777"/><path d="M1 4 L13 13 L25 4" stroke="#fff" stroke-width="1.5" fill="none"/><path d="M1 19 L10 11 M25 19 L16 11" stroke="#fff" stroke-width="1.2"/></svg>
        <span class="inbox-count">2</span>
      </span>
      <span>My Account</span>
    </div>
    <nav class="main-nav">
      <a href="#">Home</a>
      <a href="#" class="is-current">Products</a>
      <a href="#">Categories</a>
      <a href="#">About Us</a>
      <svg width="20" height="20" viewBox="0 0 20 20" aria-label="Search"><circle cx="12" cy="8" r="6" stroke="#333" stroke-width="2" fill="none"/><path d="M7.5 12.5 L2 18" stroke="#333" stroke-width="2.4" stroke-linecap="round"/></svg>
    </nav>
  </header>

  <h1 class="page-title">Luxury Getaway</h1>
  <div class="title-rule"></div>
  <nav class="breadcrumb">
    <a href="#">Home</a><span class="sep">&#9654;</span>
    <a href="#">Travel Packages</a><span class="sep">&#9654;</span>
    <span>Luxury Getaway</span>
  </nav>

  <div class="hero" role="img" aria-label="Travel photograph of the island destination: coastline and blue sea"></div>

  <h2 class="product-title">Luxury Getaway</h2>
  <div class="location">
    <svg width="20" height="26" viewBox="0 0 20 26"><path d="M10 0 C4.5 0 0 4.3 0 9.7 C0 16.5 10 26 10 26 C10 26 20 16.5 20 9.7 C20 4.3 15.5 0 10 0 Z" fill="#8a8a8a"/><circle cx="10" cy="9.5" r="3.6" fill="#fff"/></svg>
    <span>Some Island, Greece</span>
  </div>
  <div class="price"><span class="price-label">points</span><span class="price-value">2000</span></div>
  <a href="#" class="book-btn">BOOK NOW</a>

  <p class="description intro">Lorem ipsum dolor sit amet, consectetur adipiscing elit. Fusce pellentesque, tellus at lacinia tempus, odio justo rhoncus velit, et pretium dolor tortor sed neque. Nullam scelerisque diam eget urna <a href="#">hendrerit</a>, ac volutpat urna molestie. Fusce vel tortor ut dolor viverra hendrerit eget id ipsum.</p>
  <ul class="features">
    <li>5 Star Accomodation</li>
    <li>En-suite room</li>
    <li>All-inclusive</li>
  </ul>
  <p class="description outro">Vestibulum metus <a href="#">mauris</a>, scelerisque dignissim dapibus vel, mollis efficitur justo. Cras arcu felis, sodales ut diam nec, fringilla iaculis lorem.</p>

  <div class="footer-rule"></div>
  <footer>
    <p class="copyright">© 2016 Velvet Crest Club. All rights reserved.</p>
    <nav class="footer-nav"><a href="#">FAQ</a><a href="#">Legal</a><a href="#">Contact</a></nav>
  </footer>
</div>
</body>
</html>
```